Visitenkarten für ein Metallverarbeitsungsbetrieb
Zielgruppe
Metallverarbeitsungsbetrieb
spezialisiert auf Lasern
Aufgabenstellung
Passend zu unseren Logo und in den Farben, schlicht dennoch besonders

```html
<!DOCTYPE html>
<html lang="de">
<head>
<meta charset="utf-8">
<title>Visitenkarte – KMV</title>
<link href="https://fonts.googleapis.com/css2?family=Montserrat:wght@400;500;700&display=swap" rel="stylesheet">
<style>
  :root {
    --bg: #e9ebee;
    --card: #ffffff;
    --navy: #1c2a44;
    --blue: #1a8fd6;
    --grey: #5d6675;
    --rule: #c9d3de;
  }
  * { margin: 0; padding: 0; box-sizing: border-box; }
  html, body {
    width: 1200px; height: 799px; overflow: hidden;
    background: var(--bg);
    font-family: "Montserrat", Arial, sans-serif;
  }
  .card {
    position: absolute; left: 150px; top: 127px;
    width: 900px; height: 545px;
    background: var(--card);
    box-shadow: 0 10px 30px rgba(28, 42, 68, 0.15);
    overflow: hidden;
  }
  .identity { position: absolute; left: 126px; top: 66px; }
  .identity__name {
    font-size: 40px; font-weight: 700; color: var(--navy); letter-spacing: 0.5px;
  }
  .identity__role {
    margin-top: 4px; font-size: 19px; font-weight: 500; color: var(--blue);
  }
  .identity__rule {
    margin-top: 16px; width: 290px; height: 3px;
    background: linear-gradient(90deg, var(--navy) 0 45%, var(--rule) 45% 100%);
  }
  .contacts { position: absolute; left: 54px; top: 205px; list-style: none; }
  .contacts__item {
    display: flex; align-items: center; gap: 44px; margin-bottom: 34px;
  }
  .contacts__icon { width: 28px; height: 28px; flex: none; }
  .contacts__text {
    font-size: 17px; line-height: 1.35; color: var(--grey);
  }
  .brand {
    position: absolute; left: 650px; top: 200px;
    display: flex; align-items: center; gap: 14px;
  }
  .brand__dot {
    width: 38px; height: 38px; border-radius: 50%; border: 4px solid var(--navy);
  }
  .brand__name {
    font-size: 40px; font-weight: 700; color: var(--navy); letter-spacing: 2px;
  }
  .accent { position: absolute; left: 0; top: 0; width: 900px; height: 545px; }
</style>
</head>
<body>
  <div class="card">
    <svg class="accent" viewBox="0 0 900 545" aria-hidden="true">
      <polygon points="540,545 815,420 815,545" fill="#1a8fd6"/>
      <polygon points="815,420 838,410 830,545 815,545" fill="#1c2a44"/>
    </svg>

    <div class="identity">
      <h1 class="identity__name">Jonas Dorn</h1>
      <p class="identity__role">Chief Executive Officer</p>
      <div class="identity__rule"></div>
    </div>

    <ul class="contacts">
      <li class="contacts__item">
        <svg class="contacts__icon" viewBox="0 0 24 24" aria-hidden="true">
          <path d="M6.6 10.8c1.4 2.8 3.8 5.1 6.6 6.6l2.2-2.2c.3-.3.7-.4 1-.2 1.1.4 2.3.6 3.6.6.6 0 1 .4 1 1V20c0 .6-.4 1-1 1C10.6 21 3 13.4 3 4c0-.6.4-1 1-1h3.5c.6 0 1 .4 1 1 0 1.3.2 2.5.6 3.6.1.3 0 .7-.2 1z" fill="#1a8fd6"/>
        </svg>
        <p class="contacts__text">+49-351-804-2217<br>+49-351-804-2290</p>
      </li>
      <li class="contacts__item">
        <svg class="contacts__icon" viewBox="0 0 24 24" aria-hidden="true">
          <path d="M2 11 22 3l-6 18-4-7z" fill="#1c2a44"/>
          <path d="M12 14 22 3" stroke="#ffffff" stroke-width="1.4"/>
        </svg>
        <p class="contacts__text">contact@kmv.de<br>www.kmv.de</p>
      </li>
      <li class="contacts__item">
        <svg class="contacts__icon" viewBox="0 0 24 24" aria-hidden="true">
          <path d="M12 3 2 12h3v8h5v-5h4v5h5v-8h3z" fill="#1a8fd6"/>
        </svg>
        <p class="contacts__text">Werkstraße 14, Dresden, SN<br>01067</p>
      </li>
    </ul>

    <div class="brand">
      <span class="brand__dot"></span>
      <span class="brand__name">KMV</span>
    </div>
  </div>
</body>
</html>
```